Brivane - Business Cards for a new venture

create business card for a startup classified business dealing in construction materials, the cards need to have a professional look but modern, more serious than playful, one of the samples must include the official font (attached), please explore using the official colors in the company's logo

Target Market(s)

Energy sector

Contact Information for Business Card

Font styles to use
Other font styles liked:
• suissnord

Requirements
Must have
• corporate colors (in logo attached)
Nice to have
• Official font (in one of the samples) font is : suissnord
Should not have
• Cartoonish look

```html
<!DOCTYPE html>
<html lang="en">
<head>
<meta charset="utf-8">
<title>Brivane — Business Cards</title>
<link rel="stylesheet" href="https://fonts.googleapis.com/css2?family=Open+Sans:wght@400;600;700&display=swap">
<style>
  :root {
    --backdrop: #2b2c2f;
    --navy: #0f3a66;
    --card-light: #e6e6e3;
    --ink: #2a2a2a;
    --slate: #7d7f83;
    --rule: #9a9c9f;
    --white: #f2f2f2;
  }
  * { box-sizing: border-box; margin: 0; padding: 0; }
  html, body { width: 1200px; height: 900px; overflow: hidden; }
  body {
    background: var(--backdrop);
    font-family: "Open Sans", Arial, sans-serif;
    position: relative;
  }
  .card {
    position: absolute;
    left: 320px;
    width: 560px;
    height: 320px;
    border-radius: 4px;
    overflow: hidden;
    box-shadow: 0 14px 30px rgba(0,0,0,.45);
  }
  .card--front { top: 100px; background: var(--navy); }
  .card--back { top: 470px; background: var(--card-light); }

  .front-wordmark {
    position: absolute;
    top: 50%; left: 0; right: 0;
    transform: translateY(-50%);
    text-align: center;
    color: var(--white);
    font-weight: 600;
    font-size: 30px;
    letter-spacing: 8px;
    text-transform: uppercase;
  }

  .divider {
    position: absolute;
    left: 0; right: 0; top: 160px;
    height: 1px; background: var(--rule);
  }
  .divider__accent {
    position: absolute;
    right: 0; top: 158px;
    width: 120px; height: 3px; background: var(--navy);
  }
  .back-wordmark {
    position: absolute;
    left: 32px; top: 118px;
    color: var(--navy);
    font-weight: 600;
    font-size: 24px;
    letter-spacing: 5px;
    text-transform: uppercase;
  }
  .holder {
    position: absolute;
    right: 28px; top: 100px;
    text-align: right;
  }
  .holder__name { font-size: 15px; font-weight: 700; color: var(--ink); letter-spacing: .5px; text-transform: uppercase; }
  .holder__name .first { color: var(--navy); }
  .holder__title { font-size: 11px; color: var(--ink); }

  .contacts {
    position: absolute;
    left: 32px; top: 178px;
    list-style: none;
    font-size: 12px;
    color: var(--ink);
  }
  .contacts li { display: flex; align-items: center; height: 17px; }
  .contacts li.gap { margin-top: 9px; }
  .contacts svg { width: 11px; height: 11px; margin-right: 10px; fill: var(--navy); }

  .side-mark {
    position: absolute;
    right: 40px; top: 196px;
    color: var(--slate);
    font-weight: 600;
    font-size: 22px;
    letter-spacing: 5px;
    text-transform: uppercase;
  }
  .band {
    position: absolute;
    left: 0; right: 0; bottom: 12px;
    height: 30px; background: var(--navy);
  }
</style>
</head>
<body>
  <section class="card card--front">
    <div class="front-wordmark">Brivane</div>
  </section>

  <section class="card card--back">
    <div class="holder">
      <div class="holder__name"><span class="first">Daniel</span> Hart</div>
      <div class="holder__title">Managing Director</div>
    </div>
    <div class="back-wordmark">Brivane</div>
    <div class="divider"></div>
    <div class="divider__accent"></div>

    <ul class="contacts">
      <li><svg viewBox="0 0 12 12"><rect x="3" y="0.5" width="6" height="11" rx="1.2"/></svg>+100 555 0142</li>
      <li><svg viewBox="0 0 12 12"><path d="M2.5 0.8l2 2.2-1 1.5c.8 1.6 2 2.8 3.6 3.6l1.5-1 2.2 2-1 2.1C5.4 11 1 6.6.9 2z"/></svg>+100 555 0142</li>
      <li class="gap"><svg viewBox="0 0 12 12"><path d="M0.5 2.5h11v7h-11z M1 3l5 3.5L11 3" stroke="#e6e6e3" stroke-width=".8"/></svg>d.hart@brivane.co</li>
      <li><svg viewBox="0 0 12 12"><path d="M6 .5a4 4 0 0 1 4 4c0 3-4 7-4 7s-4-4-4-7a4 4 0 0 1 4-4zm0 2.5a1.5 1.5 0 1 0 0 3 1.5 1.5 0 0 0 0-3z"/></svg>Unit 12, Harbor Lane, Ardale 40215</li>
    </ul>

    <div class="side-mark">Brivane</div>
    <div class="band"></div>
  </section>
</body>
</html>
```